Harbor Crest Vitality.com Landing Page

Create a well designed home/landing page using that communicates the feeling of Harbor Crest Vitality with this sections that scroll from top to bottom -
Top section - Displays "Harbor Crest Vitality" with space for embedded YouTube video.

The following sections follow the top section -
Assess your current Harbor Crest Vitality. Complete our free life balance assessment to identify key areas where you you will most benefit.
"Learn more" call to action button

Create a Harbor Crest Vitality Learning Portal account. Get a 14 day free trial to a wealth of learning activities, motivational videos and professional presentations on our learning portal designed specifically to address the eight essential areas of Harbor Crest Vitality.
"Register now" call to action button

Get weekly reports on your progress and goal achievement. Celebrate your success each week as you review your progress on each life balance area.

Appropriate royalty free photos and graphics that fit the chosen theme you recommend.

I'm reviewing the designs. I realize that I need to clarify that Harbor Crest Vitality focuses on eight areas, not just physical fitness and meditation. Spirituality and Sense of Purpose; Fitness and Health; Relationships; Personal Finance; Recreation and Fun; Physical Environment; Personal Development and Learning; Work and Career

1 page

33a6d7
00a990
9bcb3c
2f73b3

```html
<!DOCTYPE html>
<html lang="en">
<head>
<meta charset="utf-8">
<title>Harbor Crest Vitality.com</title>
<link rel="stylesheet" href="https://fonts.googleapis.com/css2?family=Anton&family=Roboto:wght@400&family=Roboto+Slab:wght@300&display=swap">
<style>
:root{
  --sky:#33a6d7;
  --teal:#00a990;
  --lime:#9bcb3c;
  --ocean:#2f73b3;
  --ink:#2a2a2a;
  --white:#ffffff;
}
*{margin:0;padding:0;box-sizing:border-box}
html,body{width:1200px;height:2440px;overflow:hidden;background:var(--white)}
body{position:relative;font-family:"Roboto",sans-serif;color:var(--ink)}
.section{position:absolute;left:0;width:1200px;overflow:hidden}
.photo{position:absolute;inset:0}
.display{font-family:"Anton",sans-serif;font-weight:400;text-transform:uppercase;letter-spacing:-0.5px}
.btn{position:absolute;display:flex;align-items:center;justify-content:center;font-family:"Anton",sans-serif;font-size:17px;color:var(--white);text-transform:uppercase;text-decoration:none;letter-spacing:-0.2px}

/* hero */
.hero{top:0;height:635px}
.hero .photo{background:linear-gradient(100deg,var(--sky) 0%,#17b2b8 40%,#4cc07a 70%,var(--lime) 100%)}
.hero-title{position:absolute;top:122px;left:0;width:1200px;text-align:center;color:var(--white);font-size:88px;line-height:100px}
.play{position:absolute;left:542px;top:342px;width:116px;height:116px}

/* assess */
.assess{top:635px;height:568px}
.assess .photo{background:
  linear-gradient(90deg,rgba(20,130,120,.85) 0%,rgba(60,160,150,.7) 30%,rgba(170,220,215,.4) 55%,rgba(255,255,255,0) 75%),
  linear-gradient(180deg,#e8f6f5 0%,#d4ecea 45%,#f4f8f8 100%)}
.assess-title{position:absolute;left:677px;top:196px;font-size:40px;line-height:42px;color:var(--teal)}
.assess-text{position:absolute;left:677px;top:300px;width:360px;font-size:21.5px;line-height:27px;color:var(--ink)}
.assess .btn{left:677px;top:403px;width:137px;height:49px;background:var(--teal)}

/* portal */
.portal{top:1203px;height:568px}
.portal .photo{background:
  linear-gradient(180deg,rgba(0,0,0,0) 70%,rgba(30,80,150,.35) 100%),
  linear-gradient(110deg,var(--ocean) 0%,#2e8bb0 40%,#10a59a 75%,var(--teal) 100%)}
.portal-lead{position:absolute;top:138px;left:0;width:1200px;text-align:center;color:var(--white);font-size:28px;line-height:31px}
.portal-title{position:absolute;top:222px;left:0;width:1200px;text-align:center;color:var(--white);font-size:52px;line-height:58px}
.portal-text{position:absolute;top:292px;left:380px;width:440px;text-align:center;color:var(--white);font-size:13.5px;line-height:16px}
.portal .btn{left:531px;top:370px;width:137px;height:49px;background:var(--lime)}

/* reports */
.reports{top:1771px;height:570px}
.reports .photo{background:
  linear-gradient(90deg,rgba(255,255,255,.95) 0%,rgba(255,252,235,.85) 40%,rgba(240,220,120,.5) 65%,rgba(190,170,60,.55) 100%),
  linear-gradient(180deg,#fffdf0 0%,#f2e6a8 60%,#d8d0a0 100%)}
.reports-title{position:absolute;left:171px;top:178px;font-size:40px;line-height:41px;color:var(--lime)}
.reports-text{position:absolute;left:172px;top:316px;width:340px;font-size:20px;line-height:23px;color:var(--ink)}
.reports .btn{left:171px;top:407px;width:129px;height:49px;background:var(--lime)}

/* footer */
.site-footer{position:absolute;top:2341px;left:0;width:1200px;height:99px;display:flex;align-items:center;justify-content:center;font-family:"Roboto Slab",serif;font-weight:300;font-size:16px;color:#333}
</style>
</head>
<body>

<section class="section hero">
  <div class="photo" role="img" aria-label="Close view of a hand in a meditation pose by the water, tinted in a blue to green gradient"></div>
  <h1 class="hero-title display">Harbor Crest<br>Vitality</h1>
  <svg class="play" viewBox="0 0 116 116" role="img" aria-label="Play video">
    <defs>
      <linearGradient id="ringGrad" x1="0" y1="0" x2="1" y2="1">
        <stop offset="0" stop-color="#33a6d7"/>
        <stop offset="0.55" stop-color="#00a990"/>
        <stop offset="1" stop-color="#9bcb3c"/>
      </linearGradient>
    </defs>
    <circle cx="58" cy="58" r="58" fill="url(#ringGrad)"/>
    <circle cx="58" cy="58" r="44" fill="none" stroke="#ffffff" stroke-width="3"/>
    <path d="M49 39 L75 58 L49 77 Z" fill="#ffffff"/>
  </svg>
</section>

<section class="section assess">
  <div class="photo" role="img" aria-label="Woman meditating cross-legged on a wooden dock beside a calm lake with forested hills"></div>
  <h2 class="assess-title display">Assess your current<br>Harbor Crest Vitality.</h2>
  <p class="assess-text">Complete our free life balance assessment to identify key areas where you you will most benefit.</p>
  <a class="btn" href="#">Learn more</a>
</section>

<section class="section portal">
  <div class="photo" role="img" aria-label="Silhouette of a person in a yoga warrior pose on a grassy field under the sky, tinted blue to teal"></div>
  <h2 class="portal-lead display">Create a Harbor Crest Vitality<br>Learning Portal account.</h2>
  <p class="portal-title display">Get a 14 day free trial</p>
  <p class="portal-text">to a wealth of learning activities, motivational videos and professional presentations on our learning portal designed specifically to address the eight essential areas of Harbor Crest Vitality.</p>
  <a class="btn" href="#">Register now</a>
</section>

<section class="section reports">
  <div class="photo" role="img" aria-label="Smiling woman jogging outdoors in warm golden sunlight"></div>
  <h2 class="reports-title display">Get weekly reports on<br>your progress and goal<br>achievement.</h2>
  <p class="reports-text">Celebrate your success each week as you review your progress on each life balance area.</p>
  <a class="btn" href="#">Learn more</a>
</section>

<footer class="site-footer">Copyright 2020 Harbor Crest Vitality.com All Rights Reserved</footer>

</body>
</html>
```